Business card for Northland's Blue Wagon.

Good day i am looking for a business card design for my business.
The name of the business is Northland's Blue Wagon. It is a van rental business that provides a driver and helper to the customer. Customer have use to van for small moves, studio or 1 bedroom, Moving furniture like couch or kitchen cabinets.
We are available evenings, weekends and holidays.
the means to contact us is by phone at 628-947-2071; By emails at Oakridge@northlandsbluewagon.net; or by social media, Friendwall and Picshare.
You can see attached pictures of the van and or logo.

```html
<!DOCTYPE html>
<html lang="en">
<head>
<meta charset="utf-8">
<title>Northland's Blue Wagon – Business Card</title>
<link href="https://fonts.googleapis.com/css2?family=Tinos:wght@400;700&display=swap" rel="stylesheet">
<style>
  :root{
    --board:#bbbcbe;
    --red:#ed2040;
    --black:#000000;
    --white:#ffffff;
    --ink:#1a1a1a;
    --serif:"Tinos", "Times New Roman", serif;
  }
  html,body{margin:0;padding:0;overflow:hidden;}
  body{width:1200px;height:1200px;background:var(--board);position:relative;font-family:var(--serif);}
  .side-label{position:absolute;font-size:28px;color:var(--ink);margin:0;}
  .side-label.front{left:80px;top:302px;}
  .side-label.back{left:84px;top:857px;}

  .card{position:absolute;left:254px;width:840px;height:480px;overflow:hidden;}
  .card-front{top:82px;background:var(--red);}
  .card-back{top:638px;background:var(--white);}
  .card-shapes{position:absolute;inset:0;width:840px;height:480px;}

  .brand-mark{position:absolute;display:flex;flex-direction:column;align-items:center;gap:10px;}
  .brand-mark .mark-dot{border-radius:50%;}
  .brand-mark .mark-name{font-weight:700;text-align:center;white-space:nowrap;}
  .card-front .brand-mark{left:129px;top:40px;width:228px;}
  .card-front .mark-dot{width:150px;height:150px;background:var(--white);}
  .card-front .mark-name{color:var(--white);font-size:19px;}
  .card-back .brand-mark{left:38px;top:40px;width:268px;}
  .card-back .mark-dot{width:190px;height:190px;background:var(--red);}
  .card-back .mark-name{color:var(--black);font-size:22px;}

  .company-name{position:absolute;left:373px;top:84px;margin:0;color:var(--white);font-weight:700;font-size:62px;line-height:56px;}
  .tagline{position:absolute;left:0;right:0;top:278px;margin:0;text-align:center;color:var(--white);font-weight:700;font-size:35px;}
  .service-note{position:absolute;left:0;right:0;top:354px;margin:0;text-align:center;color:var(--white);font-size:29px;line-height:36px;}

  .person{position:absolute;right:74px;top:70px;text-align:right;}
  .person-name{margin:0;color:var(--white);font-weight:700;font-size:32px;line-height:36px;}
  .person-role{margin:0;color:var(--red);font-size:24px;line-height:28px;}

  .contact-list{position:absolute;left:36px;top:330px;margin:0;padding:0;list-style:none;color:var(--ink);font-size:22px;}
  .contact-list li{display:flex;align-items:center;height:40px;}
  .contact-icon{width:26px;height:26px;margin-right:10px;flex:none;}
  .find-label{font-weight:700;margin-right:12px;}
  .social-name{color:var(--red);font-size:15px;font-weight:700;margin-right:10px;}
</style>
</head>
<body>
  <p class="side-label front">Front</p>
  <p class="side-label back">Back</p>

  <section class="card card-front">
    <svg class="card-shapes" viewBox="0 0 840 480" aria-hidden="true">
      <polygon points="192,0 840,0 840,266 346,266" fill="var(--black)"/>
      <rect x="0" y="338" width="840" height="142" fill="var(--black)"/>
      <polygon points="0,445 450,445 472,480 0,480" fill="var(--red)"/>
    </svg>
    <div class="brand-mark">
      <span class="mark-dot"></span>
      <span class="mark-name">Northland's Blue Wagon</span>
    </div>
    <h1 class="company-name">Northland's<br>Blue Wagon</h1>
    <p class="tagline">Van Rental Service with Driver &amp; Helper</p>
    <p class="service-note">For small moves, studio or 1-bedroom apartments<br>and furniture transport.</p>
  </section>

  <section class="card card-back">
    <svg class="card-shapes" viewBox="0 0 840 480" aria-hidden="true">
      <polygon points="324,0 840,0 840,480 815,480" fill="var(--black)"/>
      <polygon points="697,365 815,480 654,480" fill="var(--red)"/>
    </svg>
    <div class="brand-mark">
      <span class="mark-dot"></span>
      <span class="mark-name">Northland's Blue Wagon</span>
    </div>
    <div class="person">
      <p class="person-name">TITLE NAME</p>
      <p class="person-role">DESGINATION</p>
    </div>
    <ul class="contact-list">
      <li>
        <svg class="contact-icon" viewBox="0 0 26 26" aria-hidden="true">
          <circle cx="13" cy="13" r="13" fill="var(--red)"/>
          <path d="M9 7c1 0 1.5 2.5 1.5 3s-1 1-1 1.5c.5 2 2.5 4 4.5 4.5.5 0 1-1 1.5-1s3 .5 3 1.5-1 2.5-2.5 2.5C11 19 7 15 7 9.5 7 8 8 7 9 7z" fill="var(--white)"/>
        </svg>
        <span>628-947-2071</span>
      </li>
      <li>
        <svg class="contact-icon" viewBox="0 0 26 26" aria-hidden="true">
          <circle cx="13" cy="13" r="13" fill="var(--red)"/>
          <rect x="6.5" y="8.5" width="13" height="9" fill="none" stroke="var(--white)" stroke-width="1.5"/>
          <polyline points="6.5,8.5 13,14 19.5,8.5" fill="none" stroke="var(--white)" stroke-width="1.5"/>
        </svg>
        <span>Oakridge@northlandsbluewagon.net</span>
      </li>
      <li>
        <span class="find-label">Find us on</span>
        <span class="social-name">Picshare</span>
        <span class="social-name">Friendwall</span>
        <span>Northland's Blue Wagon</span>
      </li>
    </ul>
  </section>
</body>
</html>
```